Lantern Hill Publicity is a new boutique Press Office with a small roster of well-chosen clients across an array of disciplines; from Art and Technology to Restaurants and Fashion. Based in Greenpoint Brooklyn, Lantern Hill Publicity achieves outstanding results through hard work, tenacity, efficiency and a sense of humor. We need a simple, versatile and classic design. We would like each side of the card to be white text on a black background.

Boutique

```html
<!DOCTYPE html>
<html lang="en">
<head>
<meta charset="utf-8">
<title>Lantern Hill Publicity – Business Card</title>
<link href="https://fonts.googleapis.com/css2?family=Cinzel:wght@400&family=Arimo:wght@400;700&display=swap" rel="stylesheet">
<style>
  :root {
    --stage: #5a5a5a;
    --card-black: #0c0c0c;
    --panel-black: #1b1b1b;
    --ink-light: #f2f2f2;
    --ink-soft: #c8c8c8;
    --ink-muted: #9a9a9a;
    --curve-shade: #9c9c9c;
  }
  * { box-sizing: border-box; margin: 0; padding: 0; }
  html, body { width: 1200px; height: 950px; overflow: hidden; }
  body {
    background: radial-gradient(ellipse at 50% 45%, #7a7a7a 0%, var(--stage) 60%, #3c3c3c 100%);
    position: relative;
  }
  .card {
    position: absolute;
    left: 230px;
    width: 740px;
    height: 423px;
    background: var(--card-black);
    overflow: hidden;
    box-shadow: 0 14px 30px rgba(0,0,0,0.45);
  }
  .card--front { top: 40px; }
  .card--back { top: 487px; }

  .brand {
    font-family: "Cinzel", serif;
    font-weight: 400;
    color: var(--ink-light);
    text-align: center;
    text-transform: uppercase;
  }
  .brand__main { display: block; font-size: 36px; letter-spacing: 0.1em; line-height: 1.1; }
  .brand__sub { display: block; font-size: 15px; letter-spacing: 0.6em; padding-left: 0.6em; margin-top: 6px; color: var(--ink-soft); }

  .card--front .brand {
    position: absolute;
    top: 168px;
    left: 0;
    right: 0;
  }
  .brand-url {
    position: absolute;
    top: 262px;
    left: 0;
    right: 0;
    text-align: center;
    font-family: "Arimo", sans-serif;
    font-size: 14px;
    letter-spacing: 0.32em;
    color: var(--ink-muted);
  }

  .back-curve {
    position: absolute;
    inset: 0;
    width: 740px;
    height: 423px;
  }
  .card--back .brand {
    position: absolute;
    top: 168px;
    left: 40px;
    width: 340px;
  }
  .card--back .brand__main { font-size: 30px; }
  .card--back .brand__sub { font-size: 13px; }

  .contact {
    position: absolute;
    right: 34px;
    top: 70px;
    text-align: right;
    font-family: "Arimo", sans-serif;
    color: var(--ink-light);
  }
  .contact__name { font-size: 21px; font-weight: 700; }
  .contact__role { font-size: 15px; color: var(--ink-soft); margin-top: 4px; margin-bottom: 18px; }
  .contact__address { font-size: 15px; line-height: 1.35; margin-bottom: 14px; padding-right: 28px; }
  .contact__list { list-style: none; }
  .contact__item {
    display: flex;
    justify-content: flex-end;
    align-items: center;
    gap: 10px;
    font-size: 15px;
    height: 25px;
  }
  .contact__icon { width: 18px; height: 18px; flex: none; }
</style>
</head>
<body>

<section class="card card--front" aria-label="Card front">
  <h1 class="brand"><span class="brand__main">Lantern Hill</span><span class="brand__sub">Publicity</span></h1>
  <p class="brand-url">www.lanternhillpr.com</p>
</section>

<section class="card card--back" aria-label="Card back">
  <svg class="back-curve" viewBox="0 0 740 423" aria-hidden="true">
    <path d="M438,0 C520,10 508,190 452,290 C418,350 372,398 320,423 L740,423 L740,0 Z" fill="var(--curve-shade)"/>
    <path d="M452,0 C540,10 528,195 472,295 C440,352 398,398 350,423 L740,423 L740,0 Z" fill="var(--panel-black)"/>
  </svg>

  <h2 class="brand"><span class="brand__main">Lantern Hill</span><span class="brand__sub">Publicity</span></h2>

  <div class="contact">
    <p class="contact__name">Nora Vale</p>
    <p class="contact__role">President</p>
    <p class="contact__address">412 Calder Street<br>Brooklyn, NY 11222</p>
    <ul class="contact__list">
      <li class="contact__item">555 0142 7781
        <svg class="contact__icon" viewBox="0 0 20 20" aria-label="Phone"><path d="M3 7c0-2 3-4 7-4s7 2 7 4l-3 1-1-2H7L6 8z M5 10h10l1 7H4z" fill="var(--ink-light)"/><circle cx="10" cy="13" r="1.8" fill="var(--panel-black)"/></svg>
      </li>
      <li class="contact__item">555 0199 3064
        <svg class="contact__icon" viewBox="0 0 20 20" aria-label="Mobile"><rect x="5" y="1" width="10" height="18" rx="2" fill="var(--ink-light)"/><rect x="7" y="4" width="6" height="10" fill="var(--panel-black)"/></svg>
      </li>
      <li class="contact__item">555 0163 2490
        <svg class="contact__icon" viewBox="0 0 20 20" aria-label="Fax"><rect x="5" y="2" width="10" height="6" fill="var(--ink-light)"/><rect x="2" y="8" width="16" height="9" rx="1.5" fill="var(--ink-light)"/><rect x="6" y="12" width="8" height="2" fill="var(--panel-black)"/></svg>
      </li>
      <li class="contact__item">nora@lanternhillpr.com
        <svg class="contact__icon" viewBox="0 0 20 20" aria-label="Email"><rect x="2" y="4" width="16" height="12" rx="1.5" fill="var(--ink-light)"/><path d="M3 5l7 6 7-6" stroke="var(--panel-black)" stroke-width="1.5" fill="none"/></svg>
      </li>
      <li class="contact__item">www.lanternhillpr.com
        <svg class="contact__icon" viewBox="0 0 20 20" aria-label="Website"><circle cx="10" cy="10" r="8" fill="var(--ink-light)"/><path d="M2 10h16M10 2c-3 3-3 13 0 16M10 2c3 3 3 13 0 16" stroke="var(--panel-black)" stroke-width="1.2" fill="none"/></svg>
      </li>
    </ul>
  </div>
</section>

</body>
</html>
```